Austrian finance und insurance broker needs business card design

We Need a serious looking Design for Business Card. we consult private and corporates customers in finance and insurance questions. the final design should express security and experience. We consult customers in questions of loans, Investments and insurance and have a wide range of Banks to offer. We compare several offers and select the best for our customers.

Target Market(s)

private and coporate customers with efforts in Money and insurance

Industry/Entity Type

Insurance Broker

Contact Information for Business Card

Bernhard Aigner
Geschäftsführer
staatl. geprüfter Vermögensberater und Versicherungsmakler
Tel: 0664 521 8409
office@der-brandl.at
www.der-brandl.at
Leopold Hainz Gasse 14
2183 Melkstetten
GISA Nr. 48270315 u. 51736048 (backside)

Font styles to use
Serif
Sans Serif

Requirements
Must have
• logo (designcrowd zip) and all Details
Nice to have
• makler logo design, maybe a 2 coloured Version is possible

```html
<!DOCTYPE html>
<html lang="de">
<head>
<meta charset="utf-8">
<title>Visitenkarte – Aigner Vermögensberatung</title>
<link rel="stylesheet" href="https://fonts.googleapis.com/css2?family=Nunito:wght@700&family=Open+Sans:wght@400;600&display=swap">
<style>
  :root {
    --stage: #1d1d1f;
    --card-white: #ffffff;
    --brand-blue: #2a52a0;
    --logo-blue: #1f4fb5;
    --ink-grey: #555a60;
    --accent-red: #b0223a;
    --accent-yellow: #f0d21a;
    --line-white: #ffffff;
  }
  * { margin: 0; padding: 0; box-sizing: border-box; }
  html, body { width: 1200px; height: 1003px; overflow: hidden; background: var(--stage); }
  .stage { position: relative; width: 1200px; height: 1003px; }

  .card { position: absolute; width: 640px; height: 400px; overflow: hidden; }
  .card-front { left: 60px; top: 70px; background: var(--card-white); }
  .card-back { left: 500px; top: 530px; background: var(--brand-blue); color: #fff; font-family: "Open Sans", sans-serif; }

  .accent-lines { position: absolute; inset: 0; }

  .brand-lockup { position: absolute; left: 165px; top: 150px; display: flex; align-items: center; gap: 14px; }
  .brand-dot { width: 70px; height: 70px; border: 5px solid var(--logo-blue); border-radius: 50%; }
  .brand-divider { width: 4px; height: 90px; background: var(--ink-grey); }
  .brand-text { font-family: "Nunito", sans-serif; font-weight: 700; }
  .brand-name { color: var(--logo-blue); font-size: 19px; }
  .brand-tagline { color: var(--ink-grey); font-size: 14px; margin-top: 4px; }

  .partner-badge { position: absolute; right: 36px; bottom: 40px; width: 60px; height: 60px; border-radius: 50%; background: var(--accent-red); }

  .contact-block { position: absolute; left: 0; width: 520px; text-align: center; }
  .person-name { top: 44px; font-size: 30px; letter-spacing: 0.5px; }
  .person-role { top: 86px; font-size: 20px; }
  .person-qualification { top: 130px; font-size: 19px; line-height: 30px; }
  .icon-row { top: 200px; display: flex; justify-content: center; align-items: center; gap: 10px; }
  .rule { width: 58px; height: 1px; background: #fff; margin: 0 14px; }
  .icon { width: 28px; height: 28px; border-radius: 50%; display: flex; align-items: center; justify-content: center; }
  .icon-phone { background: #fff; }
  .icon-mail { background: #e0262e; }
  .icon-plain-a { background: #21a6e6; }
  .icon-plain-b { border: 1.5px solid #fff; }
  .phone { top: 245px; font-size: 21px; font-weight: 600; }
  .web { top: 278px; font-size: 19px; }
  .pin-row { top: 320px; display: flex; justify-content: center; align-items: center; }
  .address { left: 20px; width: 600px; text-align: center; top: 362px; font-size: 14.6px; white-space: nowrap; }
</style>
</head>
<body>
<main class="stage">

  <section class="card card-front" aria-label="Vorderseite">
    <svg class="accent-lines" width="640" height="400" aria-hidden="true">
      <line x1="48" y1="0" x2="62" y2="240" stroke="#555a60" stroke-width="2.5"/>
      <line x1="88" y1="0" x2="106" y2="300" stroke="#1f4fb5" stroke-width="2.5"/>
      <line x1="128" y1="0" x2="142" y2="230" stroke="#b0223a" stroke-width="2.5"/>
    </svg>
    <div class="brand-lockup">
      <div class="brand-dot"></div>
      <div class="brand-divider"></div>
      <div class="brand-text">
        <div class="brand-name">Aigner Vermögensberatung GmbH</div>
        <div class="brand-tagline">Finanzieren, Versichern, Vorsorgen</div>
      </div>
    </div>
    <div class="partner-badge" role="img" aria-label="Partnerabzeichen Versicherungsmakler"></div>
  </section>

  <section class="card card-back" aria-label="Rückseite">
    <svg class="accent-lines" width="640" height="400" aria-hidden="true">
      <line x1="546" y1="40" x2="526" y2="300" stroke="#ffffff" stroke-width="2"/>
      <line x1="586" y1="40" x2="564" y2="335" stroke="#c8283c" stroke-width="2"/>
      <line x1="622" y1="40" x2="604" y2="300" stroke="#f0d21a" stroke-width="2"/>
    </svg>
    <div class="contact-block person-name">BERNHARD AIGNER</div>
    <div class="contact-block person-role">Geschäftsführer</div>
    <div class="contact-block person-qualification">Staatl. Geprüfter Vermögensberater und<br>Versicherungsmakler</div>
    <div class="contact-block icon-row">
      <span class="rule"></span>
      <span class="icon icon-phone">
        <svg width="16" height="16" viewBox="0 0 24 24"><path fill="#2a52a0" d="M6.6 10.8a15 15 0 0 0 6.6 6.6l2.2-2.2c.3-.3.7-.4 1-.2 1.1.4 2.3.6 3.6.6.6 0 1 .4 1 1V20c0 .6-.4 1-1 1A17 17 0 0 1 3 4c0-.6.4-1 1-1h3.5c.6 0 1 .4 1 1 0 1.3.2 2.5.6 3.6.1.3 0 .7-.2 1z"/></svg>
      </span>
      <span class="icon icon-mail">
        <svg width="16" height="12" viewBox="0 0 16 12"><rect x="0.75" y="0.75" width="14.5" height="10.5" fill="none" stroke="#fff" stroke-width="1.5"/><path d="M1 1l7 6 7-6" fill="none" stroke="#fff" stroke-width="1.5"/></svg>
      </span>
      <span class="icon icon-plain-a"></span>
      <span class="icon icon-plain-b"></span>
      <span class="rule"></span>
    </div>
    <div class="contact-block phone">0664 521 8409</div>
    <div class="contact-block web">office@der-brandl.at, www.der-brandl.at</div>
    <div class="contact-block pin-row">
      <span class="rule"></span>
      <svg width="26" height="30" viewBox="0 0 24 28" aria-hidden="true"><path fill="#fff" d="M12 1a10 10 0 0 0-10 10c0 7 10 16 10 16s10-9 10-16A10 10 0 0 0 12 1z"/><circle cx="12" cy="11" r="4" fill="#2a52a0"/></svg>
      <span class="rule"></span>
    </div>
    <div class="contact-block address">Leopold Hainz Gasse 14, 2183 Melkstetten GISA Nr. 48270315 u. 51736048 (backside)</div>
  </section>

</main>
</body>
</html>
```